Postcard flyer for body postive dance classes

We need an eye catching double sided A6 postcard for body positive dance classes. The business name is stepbloomjoy and already have a rough logo and some text that needs tidying up and putting together. The design needs to be simple and elegant. We are appealing to a diverse range of adult women with or without dance experience to join us in a safe, supportive and creative environment. We would like the design to use black, white and a soft green. The final design should communicate movement, contentment and wholeness. File with information attached.

Target Market(s)

Diverse range of adult women

Industry/Entity Type

Health And Wellness

Font styles to use
Other font styles liked:
• Candara or similar but open to suggestions

Colors
abd036
cadf82
eaf2ce
fffefb
fef9ed
fff3d1
ffffff

Requirements
Must have
• Logo and text provided.
Nice to have
• Sense of movement. Match to website colours and style.
Should not have
• Intimidating perfect body images

```html
<!DOCTYPE html>
<html lang="en">
<head>
<meta charset="utf-8">
<title>stepbloomjoy – postcard flyer</title>
<link rel="stylesheet" href="https://fonts.googleapis.com/css2?family=Lobster+Two:ital,wght@1,700&family=Oswald:wght@500&family=Arvo:wght@400;700&family=Open+Sans:wght@400&display=swap">
<style>
  :root {
    --green: #abd036;
    --green-deep: #86a92a;
    --green-pale: #eaf2ce;
    --cream: #fffefb;
    --white: #ffffff;
    --ink: #4a4a4a;
    --ink-soft: #5c5c5c;
    --rose: #c9708f;
    --lilac: #8f83a3;
    --stage: #e4e4e4;
  }
  * { box-sizing: border-box; margin: 0; padding: 0; }
  html, body { width: 1200px; height: 800px; overflow: hidden; }
  body { background: var(--stage); position: relative; font-family: "Open Sans", sans-serif; }

  .card {
    position: absolute;
    width: 540px;
    height: 360px;
    top: 220px;
    background: var(--white);
    box-shadow: 0 6px 18px rgba(0,0,0,.18);
    overflow: hidden;
  }
  .card--back { left: 40px; }
  .card--front { left: 620px; }
  .card__art { position: absolute; inset: 0; width: 100%; height: 100%; }

  .brand {
    position: absolute;
    display: flex;
    align-items: center;
    gap: 8px;
    font-family: "Arvo", serif;
    font-weight: 700;
    font-size: 22px;
    color: var(--ink);
  }
  .brand__dot { width: 14px; height: 14px; border-radius: 50%; background: var(--ink); }
  .card--back .brand { left: 108px; top: 42px; }
  .card--front .brand { left: 82px; top: 40px; }

  .invite {
    position: absolute;
    left: 70px; top: 100px; width: 300px;
    font-family: "Arvo", serif;
    font-size: 14.5px;
    line-height: 1.38;
    color: var(--ink-soft);
    text-align: center;
  }
  .location {
    position: absolute;
    left: 70px; top: 232px; width: 300px;
    text-align: center;
    font-family: "Arvo", serif;
    font-weight: 700;
    font-size: 20px;
    color: var(--ink);
  }
  .contacts {
    position: absolute;
    left: 64px; top: 266px;
    list-style: none;
    font-size: 13px;
    color: var(--ink);
  }
  .contacts li { display: flex; align-items: center; gap: 10px; height: 22px; }
  .contacts svg { width: 16px; height: 16px; fill: var(--ink); }

  .headline {
    position: absolute;
    left: 58px; top: 178px;
    font-family: "Lobster Two", cursive;
    font-style: italic;
    font-weight: 700;
    font-size: 54px;
    line-height: 0.95;
    color: var(--rose);
  }
  .headline span { display: block; }
  .headline span + span { margin-left: 28px; }
  .tagline {
    position: absolute;
    right: 24px; top: 296px;
    font-family: "Arvo", serif;
    font-size: 13px;
    line-height: 1.3;
    color: var(--ink);
    text-align: right;
  }
  .ribbon-text {
    font-family: "Oswald", sans-serif;
    font-weight: 500;
    font-size: 19px;
    fill: var(--white);
  }
</style>
</head>
<body>

<section class="card card--back" aria-label="Postcard back">
  <svg class="card__art" viewBox="0 0 540 360" aria-hidden="true">
    <defs>
      <linearGradient id="backWash" x1="0" x2="1" y1="0" y2="0">
        <stop offset="0" stop-color="#eaf2ce"/>
        <stop offset="0.7" stop-color="#fffefb"/>
        <stop offset="1" stop-color="#ffffff"/>
      </linearGradient>
    </defs>
    <rect width="540" height="360" fill="url(#backWash)"/>
    <path d="M0 0 H210 C120 8 60 22 44 64 C30 150 36 270 58 328 C200 322 400 318 540 340 V360 H0 Z" fill="var(--green)"/>
  </svg>

  <div class="brand"><span class="brand__dot"></span>stepbloomjoy</div>

  <p class="invite">If you’ve never danced before and always wanted to or you want to reignite your past love of dance, join us at stepbloomjoy to start your journey.</p>

  <h2 class="location">Harbourside/Westbay</h2>
  <ul class="contacts">
    <li><svg viewBox="0 0 16 16"><path d="M1 3h14v10H1z M2 4l6 5 6-5" fill="none" stroke="#4a4a4a" stroke-width="1.4"/></svg>mara@stepbloomjoy.com.au</li>
    <li><svg viewBox="0 0 16 16"><path d="M4 1l3 3-2 2c1 2 3 4 5 5l2-2 3 3-2 3C7 15 1 9 1 3z"/></svg>0400987612</li>
    <li><svg viewBox="0 0 16 16"><circle cx="8" cy="8" r="6.5" fill="none" stroke="#4a4a4a" stroke-width="1.4"/><path d="M1.5 8h13M8 1.5c-3 3.5-3 9.5 0 13M8 1.5c3 3.5 3 9.5 0 13" fill="none" stroke="#4a4a4a" stroke-width="1.2"/></svg>www.stepbloomjoy.com.au</li>
  </ul>
</section>

<section class="card card--front" aria-label="Postcard front">
  <svg class="card__art" viewBox="0 0 540 360">
    <defs>
      <radialGradient id="figuresTone" cx="0.5" cy="0.5" r="0.5">
        <stop offset="0" stop-color="#b07a9a"/>
        <stop offset="0.6" stop-color="#a98bb0" stop-opacity="0.7"/>
        <stop offset="1" stop-color="#eaf2ce" stop-opacity="0"/>
      </radialGradient>
      <path id="ribbonLine" d="M168 168 C300 166 420 200 540 232"/>
    </defs>
    <rect width="540" height="360" fill="var(--white)"/>
    <path d="M0 0 H54 C22 120 60 250 210 300 C310 332 430 342 540 352 V360 H0 Z" fill="var(--green)"/>
    <path d="M112 0 H540 V238 C460 210 380 178 300 178 C220 178 160 170 128 150 C150 110 126 40 112 0 Z" fill="var(--green-pale)" stroke="var(--green)" stroke-width="6"/>
    <g role="img" aria-label="Illustration of two joyful dancing figures with outstretched arms">
      <ellipse cx="390" cy="110" rx="150" ry="90" fill="url(#figuresTone)"/>
    </g>
    <path d="M150 150 C300 148 420 182 540 210 V246 C420 222 300 186 150 170 Z" fill="var(--green-deep)"/>
    <text class="ribbon-text"><textPath href="#ribbonLine">Flow with life through your inner dancer.</textPath></text>
  </svg>

  <div class="brand"><span class="brand__dot"></span>stepbloomjoy</div>

  <h1 class="headline"><span>Dance is joy,</span><span>Dance is love.</span></h1>
  <p class="tagline">Dance is at the core of our being,<br>a celebration of movement, vitality and wholeness.</p>
</section>

</body>
</html>
```